Veltoria PowerPoint Sales Deck

I need a Professional, eye-popping Veltoria Sales Slide deck that I can present to potential new customers via web conference. Veltoria is the first company to invent a digital sign-in kiosk that prints a name badge for visitors that is specifically designed for Nursing Homes and Assisted Living facilities. When a visitor sign's in the kiosk will screen the person for a criminal background, TB and to make sure they have proper insurance requirements. At the end of the day, the Veltoria sign-in kiosk adds a layer of protection to the community. I need the finished product in a PowerPoint Format

Target Market(s)

Assisted Living and Nursing Homes Owners and Operators

Requirements
Must have
• Must look professional, innovative and clean. Must have Logo.
• Color #
• Green: #3fa863
• Blue: #384275
• Need a well-designed and creative way to play a video on the 5 slides. I couldnt get it to look right?

```html
<!DOCTYPE html>
<html lang="en">
<head>
<meta charset="utf-8">
<title>Veltoria Sales Deck – Slide Overview</title>
<link rel="stylesheet" href="https://fonts.googleapis.com/css2?family=Open+Sans:wght@400;600;700&family=Ubuntu:wght@300;400&display=swap">
<style>
:root{
  --green:#3fa863;
  --blue:#384275;
  --grey:#8d8d8d;
  --grey-mid:#b4b4b4;
  --grey-light:#e9ebee;
  --text:#9a9a9a;
  --white:#ffffff;
}
*{box-sizing:border-box;margin:0;padding:0}
html,body{width:1074px;height:1200px;overflow:hidden;background:var(--white)}
body{position:relative;font-family:'Open Sans',sans-serif;color:var(--text)}
.icon-defs{position:absolute;width:0;height:0;overflow:hidden}
.slide{position:absolute;width:344px;height:191px;background:var(--white);overflow:hidden;box-shadow:0 1px 3px rgba(0,0,0,.28)}
.slide svg.art{position:absolute;left:0;top:0;width:344px;height:191px}
.title{position:absolute;left:15px;top:15px;font:300 14px/1.05 'Ubuntu',sans-serif;color:var(--blue);white-space:nowrap}
.title b{font-weight:300;color:var(--green)}
.title.rule::after{content:"";position:absolute;left:0;bottom:-3px;width:26px;height:1.5px;background:var(--green)}
.brand{position:absolute;right:12px;top:10px;font:600 7.5px 'Open Sans',sans-serif;color:var(--blue);display:flex;align-items:center;gap:3px}
.brand::before{content:"";width:7px;height:7px;border-radius:50%;background:var(--green)}
.foot{position:absolute;left:0;bottom:0;width:100%;height:7px;background:var(--blue);color:var(--white);font-size:3px;line-height:7px;padding-left:4px}
.foot .num{position:absolute;right:0;top:0;width:8px;height:7px;background:var(--green);text-align:center;font-size:3px}
.lorem{position:absolute;font-size:3.6px;line-height:4.6px;color:var(--text)}
.lorem.c{text-align:center}
.lorem.w{color:var(--white)}
.media{position:absolute;border:4px solid #2b2f36;border-radius:4px;background:linear-gradient(160deg,#e6e9ec,#aeb6bf)}
.photo{position:absolute;background:linear-gradient(135deg,#dde2e6,#b7bfc6)}
.label{position:absolute;font-size:4.5px;color:var(--blue);white-space:nowrap}
.label.g{color:var(--green)}
</style>
</head>
<body>

<svg class="icon-defs" aria-hidden="true">
  <symbol id="i-search" viewBox="0 0 10 10"><g fill="none" stroke="currentColor" stroke-width="1.2" stroke-linecap="round"><circle cx="4.2" cy="4.2" r="2.7"/><path d="M6.2 6.2l2.5 2.5"/></g></symbol>
  <symbol id="i-pencil" viewBox="0 0 10 10"><path d="M1.5 8.5l.4-2 4.9-4.9 1.6 1.6-4.9 4.9z" fill="none" stroke="currentColor" stroke-width="1" stroke-linejoin="round"/></symbol>
  <symbol id="i-rocket" viewBox="0 0 10 10"><g fill="none" stroke="currentColor" stroke-width="1" stroke-linejoin="round"><path d="M3.2 6.8C3.2 3.8 5.2 1.6 8.6 1.4 8.4 4.8 6.2 6.8 3.2 6.8z"/><circle cx="6.2" cy="3.9" r=".8"/><path d="M3.2 6.8L1.4 8.6M2.6 5.2l-1.2.2M4.8 7.4l-.2 1.2"/></g></symbol>
  <symbol id="i-gear" viewBox="0 0 10 10"><g fill="none" stroke="currentColor"><circle cx="5" cy="5" r="2.9" stroke-width="1.6" stroke-dasharray="1.3 1"/><circle cx="5" cy="5" r="1.2" stroke-width="1"/></g></symbol>
  <symbol id="i-chart" viewBox="0 0 10 10"><g fill="currentColor"><rect x="1.5" y="5.5" width="1.6" height="3"/><rect x="4.2" y="3.5" width="1.6" height="5"/><rect x="6.9" y="1.5" width="1.6" height="7"/></g></symbol>
  <symbol id="i-star" viewBox="0 0 10 10"><polygon points="5,1 6.2,3.7 9,4 6.9,5.9 7.5,8.8 5,7.3 2.5,8.8 3.1,5.9 1,4 3.8,3.7" fill="currentColor"/></symbol>
  <symbol id="i-pin" viewBox="0 0 10 10"><g fill="none" stroke="currentColor" stroke-width="1"><path d="M5 9C2.8 6.6 2 5.2 2 4a3 3 0 0 1 6 0c0 1.2-.8 2.6-3 5z"/><circle cx="5" cy="4" r="1"/></g></symbol>
  <symbol id="i-lock" viewBox="0 0 10 10"><g fill="none" stroke="currentColor" stroke-width="1"><rect x="2" y="4.5" width="6" height="4.5" rx=".6"/><path d="M3.3 4.5V3.2a1.7 1.7 0 0 1 3.4 0v1.3"/></g></symbol>
  <symbol id="i-shield" viewBox="0 0 10 10"><path d="M5 1l3.5 1.3V5c0 2-1.5 3.3-3.5 4-2-.7-3.5-2-3.5-4V2.3z" fill="none" stroke="currentColor" stroke-width="1"/></symbol>
  <symbol id="i-user" viewBox="0 0 10 10"><g fill="none" stroke="currentColor" stroke-width="1"><circle cx="5" cy="3.5" r="1.8"/><path d="M1.8 9a3.2 3.2 0 0 1 6.4 0"/></g></symbol>
  <symbol id="i-mail" viewBox="0 0 10 10"><g fill="none" stroke="currentColor" stroke-width="1"><rect x="1.2" y="2.5" width="7.6" height="5.2" rx=".5"/><path d="M1.4 2.8L5 5.6l3.6-2.8"/></g></symbol>
  <symbol id="i-cart" viewBox="0 0 10 10"><g fill="none" stroke="currentColor" stroke-width="1"><path d="M1 2h1.5l1 4.5h4.3L8.8 3.5H3"/><circle cx="4" cy="8.2" r=".6"/><circle cx="7.3" cy="8.2" r=".6"/></g></symbol>
  <symbol id="i-monitor" viewBox="0 0 10 10"><g fill="none" stroke="currentColor" stroke-width="1"><rect x="1.2" y="1.8" width="7.6" height="5" rx=".4"/><path d="M5 6.8v1.6M3.2 8.6h3.6"/></g></symbol>
  <symbol id="i-home" viewBox="0 0 10 10"><path d="M1.5 5L5 1.8 8.5 5M2.7 4v4.5h4.6V4" fill="none" stroke="currentColor" stroke-width="1"/></symbol>
  <symbol id="i-phone" viewBox="0 0 10 10"><path d="M2 2.2c.4-.5 1-.6 1.4-.2l.9 1.2c.3.4.2.9-.2 1.2l-.4.3c.4 1 1.1 1.7 2.1 2.1l.3-.4c.3-.4.8-.5 1.2-.2l1.2.9c.4.4.3 1-.2 1.4C6.6 9.5 1 3.9 2 2.2z" fill="currentColor"/></symbol>
  <symbol id="i-globe" viewBox="0 0 10 10"><g fill="none" stroke="currentColor" stroke-width=".8"><circle cx="5" cy="5" r="3.6"/><ellipse cx="5" cy="5" rx="1.6" ry="3.6"/><path d="M1.4 5h7.2"/></g></symbol>
</svg>

<!-- Row 1 -->
<section class="slide video-intro" style="left:8px;top:4px">
  <div class="photo" style="left:0;top:0;width:172px;height:86px;background:linear-gradient(120deg,#56678a,#a7b7bb)" role="img" aria-label="Soft blurred office backdrop"></div>
  <h2 class="title" style="color:#fff;top:20px">Our Video Area</h2>
  <div class="label" style="left:15px;top:52px;color:#fff;font-size:5.5px">Heading Here</div>
  <p class="lorem w" style="left:15px;top:61px;width:126px">Lorem ipsum dolor sit amet, consectetur adipiscing elit, sed do eiusmod tempor incididunt ut labore et dolore magna aliqua. Ut enim ad minim veniam.</p>
  <svg class="art" viewBox="0 0 344 191">
    <g fill="var(--blue)"><circle cx="20" cy="113" r="5"/><circle cx="20" cy="135" r="5"/><circle cx="20" cy="157" r="5"/></g>
    <use href="#i-search" x="17" y="110" width="6" height="6" color="#fff"/>
    <use href="#i-pencil" x="17" y="132" width="6" height="6" color="#fff"/>
    <use href="#i-rocket" x="17" y="154" width="6" height="6" color="#fff"/>
  </svg>
  <p class="lorem" style="left:30px;top:108px;width:110px">Lorem ipsum dolor sit amet, consectetur adipiscing elit, sed do eiusmod tempor incididunt ut labore.</p>
  <p class="lorem" style="left:30px;top:130px;width:110px">Lorem ipsum dolor sit amet, consectetur adipiscing elit, sed do eiusmod tempor incididunt ut labore.</p>
  <p class="lorem" style="left:30px;top:152px;width:110px">Lorem ipsum dolor sit amet, consectetur adipiscing elit, sed do eiusmod tempor incididunt ut labore.</p>
  <div class="media" style="left:150px;top:14px;width:186px;height:140px" role="img" aria-label="Desktop monitor playing a video of a presenter holding a visitor badge"></div>
  <div class="foot">© 2016 Veltoria. All rights reserved.<span class="num">31</span></div>
</section>

<section class="slide video-banded" style="left:365px;top:4px">
  <h2 class="title rule">Video Title <b>Goes Here</b></h2>
  <div class="brand">Veltoria</div>
  <svg class="art" viewBox="0 0 344 191">
    <rect x="0" y="96" width="176" height="95" fill="var(--blue)"/>
    <rect x="176" y="96" width="168" height="95" fill="var(--green)"/>
  </svg>
  <div class="media" style="left:100px;top:50px;width:160px;height:112px;background:linear-gradient(160deg,#5fb47c,#384275)" role="img" aria-label="Laptop playing an animated video of a nurse character with a visitor badge"></div>
</section>

<section class="slide video-side" style="left:722px;top:4px">
  <h2 class="title rule" style="top:30px">Video Title<br>Goes Here</h2>
  <div class="brand">Veltoria</div>
  <p class="lorem" style="left:15px;top:78px;width:95px">Lorem ipsum dolor sit amet, consectetur adipiscing elit, sed do eiusmod tempor incididunt ut labore et dolore magna aliqua.</p>
  <p class="lorem" style="left:15px;top:108px;width:95px">Duis aute irure dolor in reprehenderit in voluptate velit esse cillum dolore eu fugiat nulla pariatur.</p>
  <p class="lorem" style="left:15px;top:134px;width:95px">Ut enim ad minim veniam, quis nostrud exercitation ullamco laboris.</p>
  <div class="media" style="left:124px;top:28px;width:200px;height:145px" role="img" aria-label="Desktop monitor playing a video of a presenter holding a visitor badge"></div>
  <div class="foot">© 2016 Veltoria. All rights reserved.<span class="num">33</span></div>
</section>

<!-- Row 2 -->
<section class="slide video-scene" style="left:8px;top:203px">
  <div class="photo" style="left:0;top:0;width:344px;height:122px;background:linear-gradient(120deg,#e7e9ea,#c9d0cf)" role="img" aria-label="Blurred care home lobby background"></div>
  <div style="position:absolute;left:0;top:122px;width:344px;height:69px;background:var(--green)"></div>
  <h2 class="title" style="color:#5a6277;top:15px">Video Title<br>Goes Here</h2>
  <div class="media" style="left:124px;top:22px;width:200px;height:145px;background:linear-gradient(160deg,#5fb47c,#384275)" role="img" aria-label="Monitor playing an animated video of a nurse character with a member badge"></div>
  <div class="foot">© 2016 Veltoria. All rights reserved.<span class="num">34</span></div>
</section>

<section class="slide four-boxes" style="left:365px;top:203px">
  <h2 class="title rule">Four Column <b>Area</b></h2>
  <div class="brand">Veltoria</div>
  <p class="lorem" style="left:27px;top:52px;width:290px">Lorem ipsum dolor sit amet, consectetur adipiscing elit, sed do eiusmod tempor incididunt ut labore et dolore magna aliqua. Ut enim ad minim veniam, quis nostrud exercitation ullamco laboris nisi ut aliquip ex ea commodo consequat.</p>
  <svg class="art" viewBox="0 0 344 191">
    <rect x="27" y="72" width="63" height="86" fill="var(--blue)"/>
    <rect x="102" y="72" width="63" height="86" fill="var(--green)"/>
    <rect x="177" y="72" width="63" height="86" fill="var(--blue)"/>
    <rect x="252" y="72" width="63" height="86" fill="var(--green)"/>
    <g fill="#fff"><circle cx="58.5" cy="93" r="7"/><circle cx="133.5" cy="93" r="7"/><circle cx="208.5" cy="93" r="7"/><circle cx="283.5" cy="93" r="7"/></g>
    <use href="#i-star" x="54.5" y="89" width="8" height="8" color="var(--blue)"/>
    <use href="#i-rocket" x="129.5" y="89" width="8" height="8" color="var(--green)"/>
    <use href="#i-pin" x="204.5" y="89" width="8" height="8" color="var(--blue)"/>
    <use href="#i-chart" x="279.5" y="89" width="8" height="8" color="var(--green)"/>
    <g fill="#fff" font-family="Open Sans" font-size="3.6" text-anchor="middle">
      <text x="58.5" y="119">YOUR TEXT HERE</text><text x="133.5" y="119">YOUR TEXT HERE</text><text x="208.5" y="119">YOUR TEXT HERE</text><text x="283.5" y="119">YOUR TEXT HERE</text>
      <text x="58.5" y="129">Lorem ipsum dolor</text><text x="133.5" y="129">Lorem ipsum dolor</text><text x="208.5" y="129">Lorem ipsum dolor</text><text x="283.5" y="129">Lorem ipsum dolor</text>
      <text x="58.5" y="134">sit consectetur</text><text x="133.5" y="134">sit consectetur</text><text x="208.5" y="134">sit consectetur</text><text x="283.5" y="134">sit consectetur</text>
      <text x="58.5" y="139">adipiscing elit.</text><text x="133.5" y="139">adipiscing elit.</text><text x="208.5" y="139">adipiscing elit.</text><text x="283.5" y="139">adipiscing elit.</text>
    </g>
  </svg>
  <div class="foot">© 2016 Veltoria. All rights reserved.<span class="num">35</span></div>
</section>

<section class="slide four-rings" style="left:722px;top:203px">
  <h2 class="title rule">Four Column <b>Area</b></h2>
  <div class="brand">Veltoria</div>
  <p class="lorem c" style="left:40px;top:50px;width:264px">Lorem ipsum dolor sit amet, consectetur adipiscing elit, sed do eiusmod tempor incididunt ut labore et dolore magna aliqua. Ut enim ad minim veniam, quis nostrud exercitation ullamco laboris.</p>
  <svg class="art" viewBox="0 0 344 191">
    <g fill="none" stroke-width="3">
      <circle cx="68" cy="90" r="19" stroke="var(--blue)"/><circle cx="138" cy="90" r="19" stroke="var(--green)"/>
      <circle cx="207" cy="90" r="19" stroke="var(--blue)"/><circle cx="276" cy="90" r="19" stroke="var(--green)"/>
    </g>
    <g fill="none" stroke="#dcdfe4" stroke-width=".8">
      <circle cx="68" cy="90" r="14"/><circle cx="138" cy="90" r="14"/><circle cx="207" cy="90" r="14"/><circle cx="276" cy="90" r="14"/>
    </g>
    <use href="#i-chart" x="61" y="83" width="14" height="14" color="var(--blue)"/>
    <use href="#i-star" x="131" y="83" width="14" height="14" color="var(--green)"/>
    <use href="#i-rocket" x="200" y="83" width="14" height="14" color="var(--blue)"/>
    <use href="#i-pin" x="269" y="83" width="14" height="14" color="var(--green)"/>
    <g stroke="#cfd2d8" stroke-width=".5"><path d="M103 75v80M172 75v80M241 75v80"/></g>
    <g font-family="Open Sans" font-size="4.4" font-weight="700" text-anchor="middle">
      <text x="68" y="121" fill="var(--blue)">COLUMN 1</text><text x="138" y="121" fill="var(--green)">COLUMN 2</text>
      <text x="207" y="121" fill="var(--blue)">COLUMN 3</text><text x="276" y="121" fill="var(--green)">COLUMN 4</text>
    </g>
  </svg>
  <p class="lorem c" style="left:46px;top:126px;width:44px">Lorem ipsum dolor sit amet, consectetur adipiscing elit, sed do eiusmod tempor.</p>
  <p class="lorem c" style="left:116px;top:126px;width:44px">Lorem ipsum dolor sit amet, consectetur adipiscing elit, sed do eiusmod tempor.</p>
  <p class="lorem c" style="left:185px;top:126px;width:44px">Lorem ipsum dolor sit amet, consectetur adipiscing elit, sed do eiusmod tempor.</p>
  <p class="lorem c" style="left:254px;top:126px;width:44px">Lorem ipsum dolor sit amet, consectetur adipiscing elit, sed do eiusmod tempor.</p>
  <div class="foot">© 2016 Veltoria. All rights reserved.<span class="num">36</span></div>
</section>

<!-- Row 3 -->
<section class="slide hex-cluster" style="left:8px;top:402px">
  <h2 class="title rule">Shield <b>Infographic</b></h2>
  <div class="brand">Veltoria</div>
  <p class="lorem c" style="left:30px;top:46px;width:284px">Lorem ipsum dolor sit amet, consectetur adipiscing elit, sed do eiusmod tempor incididunt ut labore et dolore magna aliqua.</p>
  <svg class="art" viewBox="0 0 344 191">
    <g stroke="var(--green)" stroke-width=".8" fill="none"><path d="M106 68h4l30 36M244 78h-28l-10 16M125 133h20M200 140h59"/></g>
    <polygon points="140,102 152,95 164,102 164,122 152,129 140,122" fill="var(--green)"/>
    <polygon points="166,92 178,85 190,92 190,112 178,119 166,112" fill="var(--blue)"/>
    <polygon points="192,102 204,95 216,102 216,122 204,129 192,122" fill="var(--green)"/>
    <polygon points="153,124 165,117 177,124 177,144 165,151 153,144" fill="var(--blue)"/>
    <polygon points="179,124 191,117 203,124 203,144 191,151 179,144" fill="var(--green)"/>
    <g fill="#fff" font-family="Open Sans" font-size="3.6" text-anchor="middle"><text x="178" y="104">01</text><text x="152" y="114">02</text><text x="165" y="136">04</text><text x="191" y="136">03</text><text x="204" y="114">05</text></g>
    <circle cx="100" cy="68" r="6" fill="var(--blue)"/><use href="#i-gear" x="96.5" y="64.5" width="7" height="7" color="#fff"/>
    <circle cx="250" cy="78" r="6" fill="var(--green)"/><use href="#i-rocket" x="246.5" y="74.5" width="7" height="7" color="#fff"/>
    <circle cx="120" cy="133" r="5" fill="var(--green)"/><use href="#i-pin" x="117" y="130" width="6" height="6" color="#fff"/>
    <circle cx="265" cy="140" r="6" fill="var(--blue)"/><use href="#i-monitor" x="261.5" y="136.5" width="7" height="7" color="#fff"/>
  </svg>
  <div class="label" style="left:38px;top:63px">Your Text Goes Here</div>
  <p class="lorem" style="left:20px;top:70px;width:70px;text-align:right">Lorem ipsum dolor sit amet, consectetur adipiscing elit, sed do eiusmod tempor.</p>
  <div class="label g" style="left:260px;top:73px">Your Text Goes Here</div>
  <p class="lorem" style="left:260px;top:80px;width:70px">Lorem ipsum dolor sit amet, consectetur adipiscing elit, sed do eiusmod tempor.</p>
  <div class="label g" style="left:70px;top:128px">Your Text Goes Here</div>
  <p class="lorem" style="left:40px;top:135px;width:70px;text-align:right">Lorem ipsum dolor sit amet, consectetur adipiscing elit, sed do eiusmod.</p>
  <div class="label" style="left:275px;top:135px">Your Text Goes Here</div>
  <p class="lorem" style="left:275px;top:142px;width:62px">Lorem ipsum dolor sit amet, consectetur adipiscing elit, sed do eiusmod.</p>
  <div class="foot">© 2016 Veltoria. All rights reserved.<span class="num">37</span></div>
</section>

<section class="slide banner-rows" style="left:365px;top:402px">
  <h2 class="title rule">Shield <b>Infographic</b></h2>
  <div class="brand">Veltoria</div>
  <p class="lorem c" style="left:28px;top:46px;width:288px">Lorem ipsum dolor sit amet, consectetur adipiscing elit, sed do eiusmod tempor incididunt ut labore et dolore magna aliqua.</p>
  <svg class="art" viewBox="0 0 344 191">
    <rect x="96" y="70" width="176" height="15" fill="var(--blue)"/>
    <rect x="96" y="110" width="176" height="15" fill="var(--green)"/>
    <rect x="96" y="150" width="176" height="15" fill="var(--blue)"/>
    <rect x="74" y="67" width="22" height="22" rx="3" fill="var(--green)"/>
    <rect x="74" y="107" width="22" height="22" rx="3" fill="var(--blue)"/>
    <rect x="74" y="147" width="22" height="22" rx="3" fill="var(--green)"/>
    <use href="#i-shield" x="79" y="72" width="12" height="12" color="#fff"/>
    <use href="#i-chart" x="79" y="112" width="12" height="12" color="#fff"/>
    <use href="#i-monitor" x="79" y="152" width="12" height="12" color="#fff"/>
  </svg>
  <p class="lorem w" style="left:100px;top:72px;width:168px">Lorem ipsum dolor sit amet, consectetur adipiscing elit, sed do eiusmod tempor incididunt ut labore et dolore magna aliqua.</p>
  <p class="lorem w" style="left:100px;top:112px;width:168px">Lorem ipsum dolor sit amet, consectetur adipiscing elit, sed do eiusmod tempor incididunt ut labore et dolore magna aliqua.</p>
  <p class="lorem w" style="left:100px;top:152px;width:168px">Lorem ipsum dolor sit amet, consectetur adipiscing elit, sed do eiusmod tempor incididunt ut labore et dolore magna aliqua.</p>
  <div class="foot">© 2016 Veltoria. All rights reserved.<span class="num">38</span></div>
</section>

<section class="slide brand-panel" style="left:722px;top:402px">
  <h2 class="title rule">Shield <b>Infographic</b></h2>
  <div class="brand">Veltoria</div>
  <svg class="art" viewBox="0 0 344 191">
    <rect x="150" y="56" width="142" height="16" fill="var(--green)"/>
    <rect x="150" y="77" width="142" height="16" fill="var(--green)"/>
    <rect x="150" y="98" width="142" height="16" fill="var(--green)"/>
    <rect x="150" y="119" width="142" height="16" fill="var(--green)"/>
    <rect x="150" y="56" width="8" height="79" fill="var(--blue)"/>
    <rect x="64" y="46" width="100" height="100" rx="6" fill="var(--blue)"/>
  </svg>
  <div style="position:absolute;left:64px;top:88px;width:100px;text-align:center;font:600 11px 'Open Sans',sans-serif;color:#fff">Veltoria</div>
  <p class="lorem w" style="left:172px;top:58px;width:116px">Lorem ipsum dolor sit amet, consectetur adipiscing elit, sed do eiusmod tempor incididunt ut labore.</p>
  <p class="lorem w" style="left:172px;top:79px;width:116px">Lorem ipsum dolor sit amet, consectetur adipiscing elit, sed do eiusmod tempor incididunt ut labore.</p>
  <p class="lorem w" style="left:172px;top:100px;width:116px">Lorem ipsum dolor sit amet, consectetur adipiscing elit, sed do eiusmod tempor incididunt ut labore.</p>
  <p class="lorem w" style="left:172px;top:121px;width:116px">Lorem ipsum dolor sit amet, consectetur adipiscing elit, sed do eiusmod tempor incididunt ut labore.</p>
  <p class="lorem c" style="left:25px;top:164px;width:294px">Lorem ipsum dolor sit amet, consectetur adipiscing elit, sed do eiusmod tempor incididunt ut labore et dolore magna aliqua ut enim.</p>
  <div class="foot">© 2016 Veltoria. All rights reserved.<span class="num">39</span></div>
</section>

<!-- Row 4 -->
<section class="slide timeline" style="left:8px;top:601px">
  <h2 class="title rule">Timeline</h2>
  <div class="brand">Veltoria</div>
  <svg class="art" viewBox="0 0 344 191">
    <path d="M40 91H300" stroke="#c8cbd1" stroke-width=".8"/>
    <g stroke="#c8cbd1" stroke-width=".8"><path d="M93 75v16M177 75v16M260 75v16M136 91v14M218 91v14"/></g>
    <g font-family="Open Sans" font-size="7" text-anchor="middle" fill="#fff">
      <circle cx="40" cy="91" r="17" fill="var(--blue)"/><text x="40" y="91">2011</text>
      <circle cx="93" cy="58" r="17" fill="var(--green)"/><text x="93" y="58">2012</text>
      <circle cx="136" cy="122" r="17" fill="var(--grey-mid)"/><text x="136" y="122">2013</text>
      <circle cx="177" cy="58" r="17" fill="var(--grey-mid)"/><text x="177" y="58">2014</text>
      <circle cx="218" cy="122" r="17" fill="var(--grey-mid)"/><text x="218" y="122">2015</text>
      <circle cx="260" cy="58" r="17" fill="var(--green)"/><text x="260" y="58">2016</text>
      <circle cx="300" cy="91" r="17" fill="var(--blue)"/><text x="300" y="91">2017</text>
      <g font-size="2.8"><text x="40" y="97">Your Text</text><text x="93" y="64">Your Text</text><text x="136" y="128">Your Text</text><text x="177" y="64">Your Text</text><text x="218" y="128">Your Text</text><text x="260" y="64">Your Text</text><text x="300" y="97">Your Text</text></g>
    </g>
  </svg>
  <div class="label" style="left:258px;top:127px">Your Text Goes Here</div>
  <p class="lorem" style="left:248px;top:134px;width:80px;text-align:right">Lorem ipsum dolor sit amet, consectetur adipiscing elit, sed do eiusmod tempor incididunt ut labore.</p>
  <div class="label" style="left:15px;top:154px">Your Text Goes Here</div>
  <p class="lorem" style="left:15px;top:161px;width:150px">Lorem ipsum dolor sit amet, consectetur adipiscing elit, sed do eiusmod tempor incididunt ut labore et dolore magna aliqua.</p>
  <div class="foot">© 2016 Veltoria. All rights reserved.<span class="num">40</span></div>
</section>

<section class="slide protection-ring" style="left:365px;top:601px">
  <h2 class="title rule">Shield <b>Infographic</b></h2>
  <div class="brand">Veltoria</div>
  <svg class="art" viewBox="0 0 344 191">
    <circle cx="170" cy="113" r="44" fill="none" stroke="var(--blue)" stroke-width="1.2" stroke-dasharray="6 4"/>
    <path d="M170 88l22 8v14c0 14-10 22-22 27-12-5-22-13-22-27V96z" fill="var(--green)"/>
    <text x="170" y="116" text-anchor="middle" font-family="Open Sans" font-size="6" font-weight="600" fill="#fff">PROTECTION</text>
    <circle cx="170" cy="69" r="7" fill="var(--blue)"/><use href="#i-monitor" x="166" y="65" width="8" height="8" color="#fff"/>
    <circle cx="127" cy="100" r="7" fill="var(--blue)"/><use href="#i-user" x="123" y="96" width="8" height="8" color="#fff"/>
    <circle cx="213" cy="96" r="6" fill="var(--blue)"/><use href="#i-mail" x="209.5" y="92.5" width="7" height="7" color="#fff"/>
    <circle cx="206" cy="142" r="7" fill="var(--green)"/><use href="#i-cart" x="202" y="138" width="8" height="8" color="#fff"/>
    <circle cx="138" cy="146" r="6" fill="var(--blue)"/><use href="#i-lock" x="134.5" y="142.5" width="7" height="7" color="#fff"/>
    <use href="#i-search" x="182" y="151" width="7" height="7" color="var(--blue)"/>
    <use href="#i-home" x="147" y="69" width="6" height="6" color="var(--green)"/>
    <use href="#i-star" x="191" y="72" width="6" height="6" color="var(--green)"/>
    <circle cx="96" cy="67" r="6" fill="var(--blue)"/><use href="#i-gear" x="92.5" y="63.5" width="7" height="7" color="#fff"/>
    <circle cx="243" cy="67" r="6" fill="var(--green)"/><use href="#i-rocket" x="239.5" y="63.5" width="7" height="7" color="#fff"/>
    <circle cx="96" cy="134" r="6" fill="var(--green)"/><use href="#i-pin" x="92.5" y="130.5" width="7" height="7" color="#fff"/>
    <circle cx="252" cy="134" r="6" fill="var(--blue)"/><use href="#i-chart" x="248.5" y="130.5" width="7" height="7" color="#fff"/>
  </svg>
  <div class="label" style="left:38px;top:61px">Your Text Goes Here</div>
  <p class="lorem" style="left:24px;top:68px;width:64px;text-align:right">Lorem ipsum dolor sit amet, consectetur adipiscing elit, sed do eiusmod tempor.</p>
  <div class="label g" style="left:254px;top:61px">Your Text Goes Here</div>
  <p class="lorem" style="left:254px;top:68px;width:64px">Lorem ipsum dolor sit amet, consectetur adipiscing elit, sed do eiusmod tempor.</p>
  <div class="label g" style="left:38px;top:129px">Your Text Goes Here</div>
  <p class="lorem" style="left:24px;top:136px;width:64px;text-align:right">Lorem ipsum dolor sit amet, consectetur adipiscing elit, sed do eiusmod tempor.</p>
  <div class="label" style="left:262px;top:129px">Your Text Goes Here</div>
  <p class="lorem" style="left:262px;top:136px;width:60px">Lorem ipsum dolor sit amet, consectetur adipiscing elit, sed do eiusmod tempor.</p>
  <div class="foot">© 2016 Veltoria. All rights reserved.<span class="num">41</span></div>
</section>

<section class="slide workflow" style="left:722px;top:601px">
  <h2 class="title rule">Workflow <b>Area</b></h2>
  <div class="brand">Veltoria</div>
  <p class="lorem" style="left:15px;top:52px;width:314px">Lorem ipsum dolor sit amet, consectetur adipiscing elit, sed do eiusmod tempor incididunt ut labore et dolore magna aliqua. Ut enim ad minim veniam, quis nostrud exercitation ullamco laboris nisi ut aliquip ex ea commodo consequat.</p>
  <svg class="art" viewBox="0 0 344 191">
    <g fill="none" stroke-width="8">
      <path d="M23 120a29 29 0 0 1 58 0" stroke="var(--blue)"/>
      <path d="M81 120a28 28 0 0 0 56 0" stroke="var(--green)"/>
      <path d="M137 120a29 29 0 0 1 58 0" stroke="var(--blue)"/>
      <path d="M195 120a28 28 0 0 0 56 0" stroke="var(--green)"/>
      <path d="M251 120a29 29 0 0 1 58 0" stroke="var(--blue)"/>
    </g>
    <g font-family="Open Sans" font-size="3.6" text-anchor="middle">
      <circle cx="52" cy="103" r="5" fill="var(--blue)"/><text x="52" y="104.5" fill="#fff">1</text>
      <circle cx="109" cy="135" r="5" fill="var(--green)"/><text x="109" y="136.5" fill="#fff">2</text>
      <circle cx="166" cy="103" r="5" fill="var(--blue)"/><text x="166" y="104.5" fill="#fff">3</text>
      <circle cx="223" cy="135" r="5" fill="var(--green)"/><text x="223" y="136.5" fill="#fff">4</text>
      <circle cx="280" cy="103" r="5" fill="var(--blue)"/><text x="280" y="104.5" fill="#fff">5</text>
      <g font-size="4.4" font-weight="700" fill="var(--blue)"><text x="38" y="125">Data 1</text><text x="109" y="80">Data 2</text><text x="152" y="125">Data 3</text><text x="223" y="80">Data 4</text><text x="295" y="125">Data 5</text></g>
    </g>
  </svg>
  <p class="lorem c" style="left:22px;top:128px;width:34px">Lorem ipsum dolor sit amet, consectetur.</p>
  <p class="lorem c" style="left:92px;top:83px;width:34px">Lorem ipsum dolor sit amet, consectetur.</p>
  <p class="lorem c" style="left:136px;top:128px;width:34px">Lorem ipsum dolor sit amet, consectetur.</p>
  <p class="lorem c" style="left:206px;top:83px;width:34px">Lorem ipsum dolor sit amet, consectetur.</p>
  <p class="lorem c" style="left:279px;top:128px;width:34px">Lorem ipsum dolor sit amet, consectetur.</p>
  <div class="foot">© 2016 Veltoria. All rights reserved.<span class="num">42</span></div>
</section>

<!-- Row 5 -->
<section class="slide bar-chart" style="left:8px;top:800px">
  <h2 class="title rule">Bullet &amp; <b>Chart Area</b></h2>
  <div class="brand">Veltoria</div>
  <svg class="art" viewBox="0 0 344 191">
    <g font-family="Open Sans" font-size="3" fill="var(--grey)" text-anchor="end"><text x="50" y="65">Category 4</text><text x="50" y="90">Category 3</text><text x="50" y="115">Category 2</text><text x="50" y="140">Category 1</text></g>
    <rect x="52" y="58" width="95" height="3.5" fill="var(--grey)"/><rect x="52" y="62" width="52" height="3.5" fill="var(--green)"/><rect x="52" y="66" width="85" height="3.5" fill="var(--blue)"/>
    <rect x="52" y="83" width="35" height="3.5" fill="var(--grey)"/><rect x="52" y="87" width="48" height="3.5" fill="var(--green)"/><rect x="52" y="91" width="64" height="3.5" fill="var(--blue)"/>
    <rect x="52" y="108" width="47" height="3.5" fill="var(--grey)"/><rect x="52" y="112" width="88" height="3.5" fill="var(--green)"/><rect x="52" y="116" width="60" height="3.5" fill="var(--blue)"/>
    <rect x="52" y="133" width="36" height="3.5" fill="var(--grey)"/><rect x="52" y="137" width="58" height="3.5" fill="var(--green)"/><rect x="52" y="141" width="80" height="3.5" fill="var(--blue)"/>
    <path d="M52 55v94" stroke="#d5d7db" stroke-width=".5"/>
    <g font-family="Open Sans" font-size="2.8" fill="var(--grey)"><rect x="67" y="156" width="2" height="2" fill="var(--grey)"/><text x="70" y="158">Series 3</text><rect x="88" y="156" width="2" height="2" fill="var(--green)"/><text x="91" y="158">Series 2</text><rect x="109" y="156" width="2" height="2" fill="var(--blue)"/><text x="112" y="158">Series 1</text></g>
    <circle cx="195" cy="62" r="6" fill="var(--blue)"/><use href="#i-search" x="191.5" y="58.5" width="7" height="7" color="#fff"/>
    <circle cx="195" cy="90" r="6" fill="var(--green)"/><use href="#i-pencil" x="191.5" y="86.5" width="7" height="7" color="#fff"/>
    <circle cx="195" cy="118" r="6" fill="var(--blue)"/><use href="#i-rocket" x="191.5" y="114.5" width="7" height="7" color="#fff"/>
    <circle cx="195" cy="146" r="6" fill="var(--green)"/><use href="#i-gear" x="191.5" y="142.5" width="7" height="7" color="#fff"/>
  </svg>
  <div class="label" style="left:210px;top:56px">Category One</div>
  <p class="lorem" style="left:210px;top:63px;width:110px">Lorem ipsum dolor sit amet, consectetur adipiscing elit, sed do.</p>
  <div class="label g" style="left:210px;top:84px">Category Two</div>
  <p class="lorem" style="left:210px;top:91px;width:110px">Lorem ipsum dolor sit amet, consectetur adipiscing elit, sed do.</p>
  <div class="label" style="left:210px;top:112px">Category Three</div>
  <p class="lorem" style="left:210px;top:119px;width:110px">Lorem ipsum dolor sit amet, consectetur adipiscing elit, sed do.</p>
  <div class="label g" style="left:210px;top:140px">Category Four</div>
  <p class="lorem" style="left:210px;top:147px;width:110px">Lorem ipsum dolor sit amet, consectetur adipiscing elit, sed do.</p>
  <div class="foot">© 2016 Veltoria. All rights reserved.<span class="num">43</span></div>
</section>

<section class="slide table-area" style="left:365px;top:800px">
  <h2 class="title rule">Table <b>Area</b></h2>
  <div class="brand">Veltoria</div>
  <svg class="art" viewBox="0 0 344 191">
    <rect x="52" y="50" width="240" height="114" fill="#fff" stroke="#e3e5e8" stroke-width=".5"/>
    <rect x="52" y="50" width="96" height="30" fill="var(--blue)"/>
    <rect x="148" y="50" width="72" height="30" fill="var(--grey)"/>
    <rect x="220" y="50" width="72" height="30" fill="var(--green)"/>
    <g fill="#fff"><circle cx="184" cy="68" r="4.5"/><circle cx="256" cy="68" r="4.5"/></g>
    <use href="#i-rocket" x="181" y="65" width="6" height="6" color="var(--grey)"/>
    <use href="#i-star" x="253" y="65" width="6" height="6" color="var(--green)"/>
    <g font-family="Open Sans" font-size="4.4" font-weight="600" fill="#fff"><text x="58" y="67">Description</text><text x="184" y="59" text-anchor="middle">Column 1</text><text x="256" y="59" text-anchor="middle">Column 2</text></g>
    <g stroke="#e3e5e8" stroke-width=".4"><path d="M57 88h85M57 97h85M57 106h85M57 115h85M57 124h85M57 133h85M57 142h85M57 151h85M153 88h62M153 97h62M153 106h62M153 115h62M153 124h62M153 133h62M153 142h62M153 151h62M225 88h62M225 97h62M225 106h62M225 115h62M225 124h62M225 133h62M225 142h62M225 151h62"/></g>
    <g font-family="Open Sans" font-size="3" fill="var(--grey)">
      <text x="58" y="86">Description 1</text><text x="58" y="95">Description 2</text><text x="58" y="104">Description 3</text><text x="58" y="113">Description 4</text><text x="58" y="122">Description 5</text><text x="58" y="131">Description 6</text><text x="58" y="140">Description 7</text><text x="58" y="149">Description 8</text>
      <g text-anchor="middle" fill="#333"><text x="184" y="122">Text Column 1</text><text x="184" y="140">Text Column 1</text><text x="256" y="122">Text Column 2</text><text x="256" y="140">Text Column 2</text></g>
    </g>
    <g fill="#222"><circle cx="184" cy="84" r="1"/><circle cx="184" cy="93" r="1"/><circle cx="184" cy="102" r="1"/><circle cx="184" cy="111" r="1"/><circle cx="184" cy="129" r="1"/><circle cx="184" cy="147" r="1"/><circle cx="256" cy="84" r="1"/><circle cx="256" cy="93" r="1"/><circle cx="256" cy="102" r="1"/><circle cx="256" cy="111" r="1"/><circle cx="256" cy="129" r="1"/><circle cx="256" cy="147" r="1"/></g>
  </svg>
  <div class="foot">© 2016 Veltoria. All rights reserved.<span class="num">44</span></div>
</section>

<section class="slide donut-chart" style="left:722px;top:800px">
  <h2 class="title rule">Bullet &amp; <b>Chart Area</b></h2>
  <div class="brand">Veltoria</div>
  <svg class="art" viewBox="0 0 344 191">
    <circle cx="40" cy="62" r="6" fill="var(--blue)"/><use href="#i-search" x="36.5" y="58.5" width="7" height="7" color="#fff"/>
    <circle cx="40" cy="90" r="6" fill="var(--green)"/><use href="#i-pencil" x="36.5" y="86.5" width="7" height="7" color="#fff"/>
    <circle cx="40" cy="118" r="6" fill="var(--grey)"/><use href="#i-rocket" x="36.5" y="114.5" width="7" height="7" color="#fff"/>
    <circle cx="40" cy="146" r="6" fill="var(--grey-mid)"/><use href="#i-gear" x="36.5" y="142.5" width="7" height="7" color="#fff"/>
    <g transform="rotate(-90 245 108)" fill="none" stroke-width="10">
      <circle cx="245" cy="108" r="32" stroke="var(--blue)" stroke-dasharray="120.6 80.5"/>
      <circle cx="245" cy="108" r="32" stroke="var(--green)" stroke-dasharray="50.3 150.8" stroke-dashoffset="-120.6"/>
      <circle cx="245" cy="108" r="32" stroke="#7a7a7a" stroke-dasharray="30.2 170.9" stroke-dashoffset="-170.9"/>
      <circle cx="245" cy="108" r="32" stroke="#c3c3c3" stroke-dasharray="20.1 181" stroke-dashoffset="-201.1"/>
    </g>
    <use href="#i-chart" x="236" y="99" width="18" height="18" color="var(--blue)"/>
    <g font-family="Ubuntu" font-size="9" font-weight="300"><text x="235" y="65" fill="var(--grey)">10%</text><text x="288" y="112" fill="var(--blue)">60%</text><text x="195" y="133" fill="var(--green)">25%</text><text x="196" y="88" fill="var(--grey)">15%</text></g>
    <g font-family="Open Sans" font-size="2.8" fill="var(--grey)"><rect x="222" y="155" width="2" height="2" fill="var(--blue)"/><text x="225" y="157">1st Qtr</text><rect x="238" y="155" width="2" height="2" fill="var(--green)"/><text x="241" y="157">2nd Qtr</text><rect x="255" y="155" width="2" height="2" fill="#7a7a7a"/><text x="258" y="157">3rd Qtr</text><rect x="271" y="155" width="2" height="2" fill="#c3c3c3"/><text x="274" y="157">4th Qtr</text></g>
  </svg>
  <div class="label" style="left:55px;top:56px">Your Text Here</div>
  <p class="lorem" style="left:55px;top:63px;width:95px">Lorem ipsum dolor sit amet, consectetur adipiscing elit, sed do.</p>
  <div class="label g" style="left:55px;top:84px">Your Text Here</div>
  <p class="lorem" style="left:55px;top:91px;width:95px">Lorem ipsum dolor sit amet, consectetur adipiscing elit, sed do.</p>
  <div class="label" style="left:55px;top:112px">Your Text Here</div>
  <p class="lorem" style="left:55px;top:119px;width:95px">Lorem ipsum dolor sit amet, consectetur adipiscing elit, sed do.</p>
  <div class="label" style="left:55px;top:140px">Your Text Here</div>
  <p class="lorem" style="left:55px;top:147px;width:95px">Lorem ipsum dolor sit amet, consectetur adipiscing elit, sed do.</p>
  <div class="foot">© 2016 Veltoria. All rights reserved.<span class="num">45</span></div>
</section>

<!-- Row 6 -->
<section class="slide pricing" style="left:8px;top:999px">
  <h2 class="title rule">Pricing <b>Structure</b></h2>
  <div class="brand">Veltoria</div>
  <svg class="art" viewBox="0 0 344 191">
    <rect x="168" y="46" width="50" height="12" fill="var(--grey)"/>
    <rect x="224" y="46" width="50" height="12" fill="var(--green)"/>
    <rect x="280" y="46" width="50" height="12" fill="var(--blue)"/>
    <g fill="#f2f3f5">
      <rect x="15" y="62" width="315" height="11"/><rect x="15" y="76" width="315" height="11"/><rect x="15" y="90" width="315" height="11"/>
      <rect x="15" y="104" width="315" height="11"/><rect x="15" y="118" width="315" height="11"/><rect x="15" y="146" width="315" height="12"/>
    </g>
    <rect x="168" y="146" width="50" height="12" fill="var(--grey)"/>
    <rect x="224" y="146" width="50" height="12" fill="var(--green)"/>
    <rect x="280" y="146" width="50" height="12" fill="var(--blue)"/>
    <g font-family="Open Sans" font-size="4" text-anchor="middle" fill="#fff">
      <text x="193" y="53.5">BASIC</text><text x="249" y="53.5">SUPER</text><text x="305" y="53.5">PREMIUM</text>
      <text x="193" y="153.5">$200</text><text x="249" y="153.5">$500</text><text x="305" y="153.5">$800</text>
    </g>
    <g font-family="Open Sans" font-size="4" fill="#333">
      <text x="32" y="56" font-size="5" font-weight="600">Choose Your Plan</text>
      <text x="20" y="69">•  Description One</text><text x="20" y="83">•  Description Two</text><text x="20" y="97">•  Description Three</text><text x="20" y="111">•  Description Four</text><text x="20" y="125">•  Description Five</text>
      <text x="30" y="153.5" font-weight="700">Price</text>
      <g text-anchor="middle"><text x="193" y="69">0</text><text x="249" y="69">5</text><text x="305" y="69">10</text><text x="193" y="83">0</text><text x="249" y="83">5</text><text x="305" y="83">10</text></g>
    </g>
    <g fill="none" stroke="#333" stroke-width=".6">
      <circle cx="193" cy="95.5" r="3"/><circle cx="249" cy="95.5" r="3"/><circle cx="305" cy="95.5" r="3"/>
      <circle cx="193" cy="109.5" r="3"/><circle cx="249" cy="109.5" r="3"/><circle cx="305" cy="109.5" r="3"/>
      <circle cx="193" cy="123.5" r="3"/><circle cx="249" cy="123.5" r="3"/><circle cx="305" cy="123.5" r="3"/>
      <path d="M191.5 95.5l1 1 2-2M247.5 95.5l1 1 2-2M303.5 95.5l1 1 2-2M303.5 109.5l1 1 2-2M303.5 123.5l1 1 2-2"/>
      <path d="M191.5 108l3 3M194.5 108l-3 3M247.5 108l3 3M250.5 108l-3 3M191.5 122l3 3M194.5 122l-3 3M247.5 122l3 3M250.5 122l-3 3"/>
    </g>
    <text x="30" y="166" font-family="Open Sans" font-size="3" fill="#333">Sales Representative, please call 555.010.2041 or email <tspan fill="var(--blue)" text-decoration="underline">sales@veltoria-mail.com</tspan></text>
  </svg>
  <div class="foot">© 2016 Veltoria. All rights reserved.<span class="num">46</span></div>
</section>

<section class="slide team" style="left:365px;top:999px">
  <div class="photo" style="left:0;top:0;width:114px;height:184px;background:linear-gradient(160deg,#eef0f2,#aab3bd)" role="img" aria-label="Doctor in a white coat holding a clipboard"></div>
  <div style="position:absolute;left:0;top:150px;width:114px;height:26px;background:rgba(56,66,117,.75);color:#fff;font:300 10px/26px 'Ubuntu',sans-serif;padding-left:12px">Meet Our Team</div>
  <div class="brand">Veltoria</div>
  <svg class="art" viewBox="0 0 344 191">
    <g role="img" aria-label="Team member portraits">
      <circle cx="141" cy="34" r="18" fill="#c9ced4"/>
      <circle cx="190" cy="79" r="13" fill="#c9ced4"/><circle cx="281" cy="79" r="13" fill="#c9ced4"/>
      <circle cx="190" cy="140" r="13" fill="#c9ced4"/><circle cx="281" cy="140" r="13" fill="#c9ced4"/>
    </g>
    <g font-family="Open Sans" text-anchor="middle">
      <g font-size="4.4" fill="var(--grey)"><text x="165" y="30" text-anchor="start">Owen Hartley</text><text x="190" y="100">Luke Brennan</text><text x="281" y="100">Adam Keller</text><text x="190" y="161">Noah Pryce</text><text x="281" y="161">Clara Vance</text></g>
      <g font-size="3.4" fill="var(--green)"><text x="165" y="35" text-anchor="start">President &amp; CEO</text><text x="190" y="104">VP Marketing</text><text x="281" y="104">VP Finance</text><text x="190" y="165">VP of Business Development</text><text x="281" y="165">Manager Marketing</text></g>
      <g font-size="2.8" fill="var(--grey)"><text x="165" y="40" text-anchor="start">team@veltoria-mail.com</text><text x="190" y="108">team@veltoria-mail.com</text><text x="281" y="108">team@veltoria-mail.com</text><text x="190" y="169">team@veltoria-mail.com</text><text x="281" y="169">team@veltoria-mail.com</text></g>
    </g>
  </svg>
  <div class="foot">© 2016 Veltoria. All rights reserved.<span class="num">47</span></div>
</section>

<section class="slide contact" style="left:722px;top:999px">
  <div class="photo" style="left:0;top:0;width:344px;height:191px;background:linear-gradient(120deg,#5d6d94,#8f9fb4)" role="img" aria-label="Visitor sign-in kiosk tablet in a care home entrance"></div>
  <div style="position:absolute;left:34px;top:0;width:122px;height:191px;background:var(--blue)"></div>
  <div class="brand" style="left:58px;right:auto;top:26px;font-size:9px;color:#fff">Veltoria</div>
  <div style="position:absolute;left:46px;top:66px;font:300 12px 'Ubuntu',sans-serif;color:#fff">Our Contact</div>
  <svg class="art" viewBox="0 0 344 191">
    <use href="#i-home" x="46" y="95" width="7" height="7" color="#fff"/>
    <use href="#i-phone" x="46" y="114" width="7" height="7" color="#fff"/>
    <use href="#i-mail" x="46" y="129" width="7" height="7" color="#fff"/>
    <use href="#i-globe" x="46" y="144" width="7" height="7" color="#fff"/>
    <g fill="#fff"><circle cx="78" cy="176" r="4"/><circle cx="89" cy="176" r="4"/><circle cx="100" cy="176" r="4"/></g>
    <g font-family="Open Sans" font-size="4.2" fill="#fff">
      <text x="57" y="97">48 Harbor Lane</text><text x="57" y="102">Fairview 20415</text>
      <text x="57" y="120">(555) 010-2040</text>
      <text x="57" y="135">hello@veltoria-mail.com</text>
      <text x="57" y="150">www.veltoria-kiosk.com</text>
    </g>
    <g font-family="Open Sans" fill="#fff" text-anchor="middle">
      <text x="249" y="117" font-size="12" font-weight="700">THANK YOU</text>
      <text x="249" y="126" font-size="4.4">For Your Precious Time</text>
      <text x="249" y="137" font-size="4">Stop by our office or give us a call!</text>
      <text x="249" y="143" font-size="4">We would love to hear from you.</text>
    </g>
  </svg>
</section>

</body>
</html>
```